Cedar Gate Labradoodle web design

We're a new labradoodle breeder in Charleston, SC in need of a web design.

Our name is Cedar Gate Labradoodles.

Site we like: http://www.pebblefernlabradoodles.example/
http://www.quintbrookdoodles.example/

Logo Font:
The ''Cedar Gate'' font is called TestarossaNF and is available freely at http://www.typevatsample.example/veltrano-kx.font.  The ''Labradoodles'' font is called Worstveld Sling Extra and is available freely at http://www.glyphcrateonline.example/BrimholtDashHeavy.php.

Requirements
Must have
• Our logo
1. Home page
2. Labradoodle F.A.Q.
3. Our doodles
4. Availability
5. Adoption Process
6. Contact us
Link/badge icon for Health Guarantee
Nice to have
• Color and font to match the logo.

An area to add pictures
Should not have
• Rainbows
Rainbow colors

```html
<!DOCTYPE html>
<html lang="en">
<head>
<meta charset="utf-8">
<title>Cedar Gate Labradoodles</title>
<link rel="stylesheet" href="https://fonts.googleapis.com/css2?family=Cinzel:wght@400;700&family=PT+Sans:ital,wght@0,400;1,400&display=swap">
<style>
  :root {
    --pink-deep: #e0365d;
    --pink-mid: #ee7f98;
    --pink-soft: #eaa9b7;
    --pink-pale: #ead8da;
    --pink-text: #e6658a;
    --brown: #3b2719;
    --body-text: #4a3b33;
    --beige: #e8dccc;
    --white: #ffffff;
    --photo-red: #8a4328;
    --photo-dark: #2b1f19;
    --grey: #7a7a7a;
  }
  html, body { margin: 0; padding: 0; }
  body {
    width: 833px; height: 1200px; overflow: hidden; position: relative;
    background: var(--white);
    font-family: "PT Sans", Arial, sans-serif; color: var(--body-text);
  }
  .page { position: absolute; inset: 0; }
  .abs { position: absolute; }

  /* header */
  .header-band {
    left: 0; top: 0; width: 833px; height: 392px;
    background: linear-gradient(180deg, var(--pink-pale) 0%, #e9c2c8 60%, var(--pink-soft) 100%);
  }
  .header-rule { left: 0; top: 392px; width: 833px; height: 4px; background: var(--pink-deep); }
  .main-nav {
    left: 0; top: 0; width: 833px; height: 28px;
    background: linear-gradient(180deg, #f7a3b5 0%, var(--pink-mid) 60%, #e86384 100%);
  }
  .main-nav a {
    position: absolute; top: 7px; color: var(--white); text-decoration: none;
    font-family: "Cinzel", Georgia, serif; font-size: 12px; letter-spacing: .3px;
  }
  .hero {
    left: 61px; top: 56px; width: 711px; height: 311px;
    background: radial-gradient(ellipse at 55% 45%, #b0603c 0%, var(--photo-red) 45%, #4e2a1c 100%);
    box-shadow: 0 6px 10px rgba(0,0,0,.3);
  }
  .slider-dots { left: 696px; top: 66px; display: flex; gap: 8px; }
  .slider-dots span { width: 7px; height: 7px; border-radius: 50%; background: rgba(255,255,255,.55); }
  .slider-dots span:first-child { background: var(--white); }

  .brand {
    left: 24px; top: 12px; width: 232px; height: 232px; border-radius: 50%;
    background: var(--white); border: 6px solid var(--pink-mid);
    box-sizing: border-box; display: flex; align-items: center; justify-content: center;
    box-shadow: 0 4px 8px rgba(0,0,0,.25);
  }
  .brand-name {
    font-family: "Cinzel", Georgia, serif; font-weight: 700; color: var(--brown);
    text-align: center; font-size: 22px; line-height: 1.25;
  }

  /* welcome */
  .welcome {
    left: 0; top: 396px; width: 833px; height: 59px; margin: 0;
    display: flex; align-items: center; justify-content: center;
    font-family: "Cinzel", Georgia, serif; font-weight: 400; font-size: 22px;
    color: var(--brown); letter-spacing: .4px;
  }
  .welcome-rule { left: 0; top: 455px; width: 833px; height: 5px; background: var(--pink-deep); }

  /* content */
  .feature-photo {
    left: 61px; top: 505px; width: 344px; height: 227px;
    background: linear-gradient(160deg, #c7955c 0%, #a8855e 40%, var(--photo-dark) 70%, #c9a19a 100%);
    box-shadow: 0 8px 10px -4px rgba(0,0,0,.35);
  }
  .section-title {
    font-family: "Cinzel", Georgia, serif; font-weight: 400; font-size: 14.5px;
    color: var(--brown); margin: 0; letter-spacing: .6px;
  }
  .section-text { font-size: 10.2px; line-height: 13px; margin: 0; color: var(--body-text); }
  .read-more {
    font-style: italic; font-size: 10.5px; color: var(--pink-text); text-decoration: none;
    text-align: right;
  }
  .thumb { left: 424px; width: 106px; height: 106px; }
  .thumb-1 { top: 505px; background: linear-gradient(160deg, #5a6b7a, #7c6653 60%, #3b2e26); }
  .thumb-2 { top: 627px; background: linear-gradient(160deg, #8a8a7c, #eeeae4 45%, #6a6660); }
  .thumb-3 { top: 747px; background: linear-gradient(160deg, #d9b29a, #3a2721 50%, #d7aa92); }
  .teaser { left: 546px; width: 227px; }
  .scrollbar { left: 791px; top: 522px; width: 6px; height: 320px; border-radius: 3px; background: var(--grey); }

  /* footer */
  .footer-band {
    left: 0; top: 883px; width: 833px; height: 35px;
    background: linear-gradient(180deg, #ea6f8c, var(--pink-mid));
  }
  .footer-body { left: 0; top: 918px; width: 833px; height: 265px; background: var(--beige); }
  .footer-brand {
    left: 118px; top: 862px; width: 114px; height: 108px; border-radius: 50%;
    background: var(--white); border: 4px solid var(--pink-mid); box-sizing: border-box;
    display: flex; align-items: center; justify-content: center;
  }
  .footer-brand .brand-name { font-size: 11px; }
  .footer-nav { left: 61px; top: 978px; margin: 0; padding: 0; list-style: none; }
  .footer-nav li { height: 27.2px; }
  .footer-nav a {
    font-family: "Cinzel", Georgia, serif; font-size: 15px; color: var(--brown);
    text-decoration: none; letter-spacing: .4px;
  }
  .contact-form { left: 304px; top: 940px; width: 240px; }
  .contact-form .section-title { font-size: 15px; margin-bottom: 6px; }
  .field {
    display: block; width: 239px; box-sizing: border-box; border: 1px solid #ddd;
    background: var(--white); font-family: "PT Sans", Arial, sans-serif;
    font-size: 10.5px; color: #222; padding: 4px 7px; margin: 0;
  }
  .field-name { position: absolute; top: 25px; height: 21px; }
  .field-email { position: absolute; top: 61px; height: 21px; }
  .field-message { position: absolute; top: 93px; height: 82px; resize: none; }
  .submit {
    position: absolute; left: 180px; top: 186px; width: 59px; height: 24px;
    border: none; border-radius: 3px; color: var(--white); font-size: 10px;
    font-family: "PT Sans", Arial, sans-serif;
    background: linear-gradient(180deg, #f6a7b8, #ea7f97);
  }
  .guarantee-badge { left: 627px; top: 961px; width: 153px; height: 153px; }

  .copyright {
    left: 0; top: 1183px; width: 833px; height: 17px; margin: 0;
    background: #e99aac; text-align: center;
    font-family: "Cinzel", Georgia, serif; font-size: 8px; line-height: 17px;
    color: #c9305a; letter-spacing: .3px;
  }
</style>
</head>
<body>
<div class="page">

  <header>
    <div class="abs header-band"></div>
    <nav class="abs main-nav">
      <a href="#" style="left:285px">Home</a>
      <a href="#" style="left:350px">Availability</a>
      <a href="#" style="left:450px">Adoption</a>
      <a href="#" style="left:537px">Our Doodles</a>
      <a href="#" style="left:651px">Contact</a>
      <a href="#" style="left:733px">F.A.Q.</a>
    </nav>
    <div class="abs hero" role="img" aria-label="Slideshow photo of a red labradoodle resting on a wooden floor"></div>
    <div class="abs slider-dots"><span></span><span></span><span></span><span></span></div>
    <div class="abs brand"><span class="brand-name">Cedar Gate<br>Labradoodles</span></div>
    <div class="abs header-rule"></div>
  </header>

  <h1 class="abs welcome">Welcome to Cedar Gate Labradoodles</h1>
  <div class="abs welcome-rule"></div>

  <main>
    <div class="abs feature-photo" role="img" aria-label="Photo of a black labradoodle puppy chewing a yellow toy"></div>
    <section class="abs" style="left:61px; top:755px; width:348px;">
      <h2 class="section-title">About Us</h2>
      <p class="section-text" style="margin-top:12px">Proin gravida nibh vel velit auctor aliquet. Aenean sollicitudin, lorem quis bibendum auctor, nisi elit consequat ipsum, nec sagittis sem nibh id elit. Proin gravida nibh vel velit auctor aliquet. Aenean sollicitudin, lorem quis bibendum auctor.</p>
      <div class="read-more" style="margin-top:3px">Continue reading...</div>
    </section>

    <div class="abs thumb thumb-1" role="img" aria-label="Photo of a labradoodle for the puppy application"></div>
    <section class="abs teaser" style="top:503px">
      <h2 class="section-title">Puppy Application</h2>
      <p class="section-text" style="margin-top:12px">Proin gravida nibh vel velit auctor aliquet. Aenean sollicitudin, lorem quis bibendum auctor, nisi elit consequat ipsum, nec sagittis sem nibh id elit.</p>
      <div class="read-more" style="margin-top:14px">Continue reading...</div>
    </section>

    <div class="abs thumb thumb-2" role="img" aria-label="Photo of a white labradoodle for the health guarantee"></div>
    <section class="abs teaser" style="top:624px">
      <h2 class="section-title">Health Guarantee</h2>
      <p class="section-text" style="margin-top:12px">Proin gravida nibh vel velit auctor aliquet. Aenean sollicitudin, lorem quis bibendum auctor, nisi elit consequat ipsum, nec sagittis sem nibh id elit.</p>
      <div class="read-more" style="margin-top:14px">Continue reading...</div>
    </section>

    <div class="abs thumb thumb-3" role="img" aria-label="Photo of a newborn puppy held in a hand for the blog"></div>
    <section class="abs teaser" style="top:745px">
      <h2 class="section-title">Blog</h2>
      <p class="section-text" style="margin-top:18px">Proin gravida nibh vel velit auctor aliquet. Aenean sollicitudin, lorem quis bibendum auctor, nisi elit consequat ipsum, nec sagittis sem nibh id elit.</p>
      <div class="read-more" style="margin-top:14px">Continue reading...</div>
    </section>

    <div class="abs scrollbar"></div>
  </main>

  <footer>
    <div class="abs footer-band"></div>
    <div class="abs footer-body"></div>
    <div class="abs footer-brand"><span class="brand-name">Cedar Gate<br>Labradoodles</span></div>

    <ul class="abs footer-nav">
      <li><a href="#">Home</a></li>
      <li><a href="#">Availability</a></li>
      <li><a href="#">Adoption</a></li>
      <li><a href="#">Our Doodles</a></li>
      <li><a href="#">Contact Us</a></li>
      <li><a href="#">FAQ</a></li>
    </ul>

    <form class="abs contact-form">
      <h2 class="section-title">Contact Us</h2>
      <input class="field field-name" type="text" value="Name" aria-label="Name">
      <input class="field field-email" type="text" value="Email" aria-label="Email">
      <textarea class="field field-message" aria-label="Message"></textarea>
      <button class="submit" type="button">Submit</button>
    </form>

    <svg class="abs guarantee-badge" viewBox="0 0 153 153" role="img" aria-label="Health guarantee badge">
      <defs>
        <radialGradient id="badgeMetal" cx="40%" cy="35%" r="70%">
          <stop offset="0" stop-color="#f4f4f4"/>
          <stop offset="0.6" stop-color="#bdbdbd"/>
          <stop offset="1" stop-color="#8d8d8d"/>
        </radialGradient>
      </defs>
      <circle cx="76.5" cy="76.5" r="74" fill="url(#badgeMetal)"/>
      <circle cx="76.5" cy="76.5" r="54" fill="none" stroke="#9a9a9a" stroke-width="1.5"/>
    </svg>

    <p class="abs copyright">Copyright©2013 Cedar Gate Labradoodles All Rights Reserved.</p>
  </footer>

</div>
</body>
</html>
```